Halloway Crest Backers Guild business cards

Create a single-sided business card for the Halloway Crest Backers Guild based on the attached logo.
The additional data fields include Name, Title, Email, Phone, and website.
Please use the following as sample data:
Name: Dean Varrow
Title: Co-Founder / Investor
Email: deanvarrow@mailtern.net
Phone: 555-314-2706
Website: www.hcbackersguild.com

Target Market(s)

Start ups, entrepreneurs, venture capitalists

Industry/Entity Type

Investment

Contact Information for Business Card

Professional business card. Technology company.

Font styles to use
Serif
Sans Serif

Requirements
Must have
• Include the HCBG logo (attached)
• Name
• Title
• Email
• Phone
• Website
Should not have
• Cute, cartoony

```html
<!DOCTYPE html>
<html lang="en">
<head>
<meta charset="utf-8">
<title>Halloway Crest Backers Guild – Business Card</title>
<link rel="stylesheet" href="https://fonts.googleapis.com/css2?family=Open+Sans:ital,wght@0,400;0,600;1,400;1,700&display=swap">
<style>
  :root {
    --stage-bg: #c9c9cb;
    --card-dark-start: #0b0b0b;
    --card-dark-end: #3a3a3a;
    --card-light: #ffffff;
    --brand-green: #3a9a5c;
    --text-grey: #5a5a5a;
    --text-strong: #4a4a4a;
    --radius: 26px;
  }
  * { box-sizing: border-box; margin: 0; padding: 0; }
  html, body {
    width: 1200px;
    height: 863px;
    overflow: hidden;
  }
  body {
    background: var(--stage-bg);
    font-family: "Open Sans", Arial, sans-serif;
    display: flex;
    flex-direction: column;
    align-items: center;
    justify-content: center;
    gap: 40px;
  }
  .card {
    position: relative;
    width: 630px;
    height: 360px;
    border-radius: var(--radius);
    box-shadow: 0 10px 24px rgba(0, 0, 0, 0.25);
  }
  .card--front {
    background: linear-gradient(135deg, var(--card-dark-start) 0%, #161616 55%, var(--card-dark-end) 100%);
    display: flex;
    align-items: center;
    justify-content: center;
  }
  .card--back {
    background: var(--card-light);
  }
  .brand {
    display: flex;
    align-items: center;
    gap: 16px;
  }
  .brand__mark {
    width: 46px;
    height: 46px;
    background: var(--brand-green);
    flex-shrink: 0;
  }
  .brand__rule {
    width: 1px;
    height: 70px;
    background: var(--brand-green);
  }
  .brand__name {
    color: var(--brand-green);
    font-weight: 400;
    font-size: 32px;
    line-height: 1.05;
  }
  .card--back .brand {
    position: absolute;
    top: 92px;
    right: 44px;
    gap: 12px;
  }
  .card--back .brand__mark { width: 34px; height: 34px; }
  .card--back .brand__rule { height: 54px; }
  .card--back .brand__name { font-size: 23px; }
  .person {
    position: absolute;
    left: 48px;
    top: 60px;
    color: var(--text-grey);
  }
  .person__name {
    font-size: 20px;
    font-weight: 700;
    font-style: italic;
    color: var(--text-strong);
  }
  .person__title {
    font-size: 16px;
    margin-top: 4px;
  }
  .contact {
    position: absolute;
    left: 48px;
    top: 170px;
    color: var(--text-grey);
    font-size: 19px;
    line-height: 1.35;
    list-style: none;
  }
  .website {
    position: absolute;
    right: 44px;
    bottom: 36px;
    color: var(--brand-green);
    font-size: 20px;
  }
</style>
</head>
<body>
  <section class="card card--front" aria-label="Card front">
    <div class="brand">
      <span class="brand__mark"></span>
      <span class="brand__rule"></span>
      <span class="brand__name">Halloway Crest<br>Backers Guild</span>
    </div>
  </section>

  <section class="card card--back" aria-label="Card back">
    <div class="person">
      <p class="person__name">Dean Varrow</p>
      <p class="person__title">Co-Founder / Investor</p>
    </div>
    <ul class="contact">
      <li class="contact__phone">555-314-2706</li>
      <li class="contact__email">deanvarrow@mailtern.net</li>
    </ul>
    <div class="brand">
      <span class="brand__mark"></span>
      <span class="brand__rule"></span>
      <span class="brand__name">Halloway Crest<br>Backers Guild</span>
    </div>
    <p class="website">www.hcbackersguild.com</p>
  </section>
</body>
</html>
```